2 sided 5x7 Flyer for Lantern Ledger advertising Bookkeeping Services and BookWise Classes

I need a flyer that we will give out to business owners and at trade shows that will advertise our Bookkeeping Services and BookWise Cloud Classes.
Bookkeeping services side should focus on how we treasure the clients business and our available bookkeeping & CFO Services. Should briefly mention that Tax Planning & Tax Preparation Services are available.

The Bookwise Cloud Classes side should have the BookWise Certified PRoMentor Logo. Classes are taught virtually and in person. Have webaddress to sign up to take the classes: https://www.lanternledger.com/bookwise/

Target Market(s)

Business Owners

Industry/Entity Type

Accountant

Requirements
Must have
• Logo on each side.
Address, phone number
Match website.
Nice to have
• Picture of Doris Venn, attached
Should not have
• No cartoony feel

```html
<!DOCTYPE html>
<html lang="en">
<head>
<meta charset="utf-8">
<title>Lantern Ledger – Bookkeeping &amp; BookWise Classes Flyer</title>
<link href="https://fonts.googleapis.com/css2?family=Open+Sans:wght@400;600;700;800&display=swap" rel="stylesheet">
<style>
  :root{
    --purple:#5b1f5e;
    --purple-deep:#3e1141;
    --gold:#c9a03a;
    --gold-light:#e3c46a;
    --green:#2e9e4c;
    --badge:#2b2b2b;
    --white:#ffffff;
    --stage:#dcdcdc;
  }
  *{box-sizing:border-box;margin:0;padding:0}
  html,body{width:887px;height:1200px;overflow:hidden}
  body{background:var(--stage);font-family:"Open Sans",Arial,sans-serif;position:relative}
  .card{position:absolute;left:153px;width:582px;height:418px;background:var(--white);overflow:hidden}
  .card--services{top:144px}
  .card--classes{top:603px}
  .card svg.bg{position:absolute;inset:0}
  .abs{position:absolute}

  .brand{display:flex;align-items:center;gap:8px;color:var(--gold);font-weight:700;font-size:19px;letter-spacing:.3px;text-transform:uppercase;white-space:nowrap}
  .brand__dot{width:26px;height:26px;border-radius:50%;background:var(--gold)}

  .headline{left:23px;top:64px;color:var(--gold);font-weight:700;font-size:20px;line-height:24px}
  .tab{background:var(--gold);color:var(--white);font-weight:700;text-transform:uppercase;display:flex;align-items:center;border-radius:0 12px 0 12px}
  .tab--services{left:14px;top:133px;width:222px;height:24px;font-size:13px;padding-left:16px}
  .tab--classes{left:20px;top:20px;width:300px;height:26px;font-size:14px;padding-left:22px}

  .ticks{list-style:none;color:var(--white);font-size:13px}
  .ticks li{position:relative;padding-left:20px;height:19.6px;line-height:19.6px;white-space:nowrap}
  .ticks li::before{content:"";position:absolute;left:0;top:5px;width:10px;height:10px;border-radius:50%;background:var(--white)}
  .ticks li::after{content:"";position:absolute;left:2.5px;top:8px;width:3px;height:3px;border-right:1.5px solid var(--purple);border-top:1.5px solid var(--purple);transform:rotate(45deg)}
  .ticks--services{left:20px;top:171px}

  .tax-badge{left:222px;top:230px;width:112px;height:112px;border-radius:50%;background:var(--gold);border:3px solid var(--white);color:var(--white);font-size:9.5px;font-weight:700;text-align:center;display:flex;align-items:center;justify-content:center;line-height:12px;text-transform:uppercase}
  .schedule{color:var(--purple-deep);font-weight:700;font-size:10.5px;text-transform:uppercase}
  .call{color:var(--white);font-weight:700;font-size:18px;white-space:nowrap}
  .site{color:var(--purple);font-weight:700;font-size:11px}

  .classes-lead{left:20px;top:64px;color:var(--gold-light);font-weight:700;font-size:13.5px;line-height:18px;text-transform:uppercase}
  .ticks--classes{font-size:13px}
  .ticks--classes li{height:21px;line-height:21px}
  .ticks--classes li.ticks__small{font-size:11.5px}
  .signup{left:75px;top:201px;width:456px;height:19px;border-radius:10px;background:var(--green);color:var(--white);font-weight:700;font-size:11px;display:flex;align-items:center;justify-content:center;gap:8px}
  .signup .url{font-weight:600}
  .delivery{left:0;width:582px;top:229px;text-align:center;color:var(--white);font-size:11px}
  .partner-badge{left:460px;top:12px;width:98px;height:98px;border-radius:50%;background:var(--badge);border:3px solid var(--white)}

  .portrait{left:27px;top:277px;width:100px;height:100px;border-radius:50%;border:4px solid var(--gold);background:radial-gradient(circle at 50% 40%,#d9b9a4,#7a4f3a 75%)}
  .person{left:161px;top:283px;color:var(--gold);font-weight:700;font-size:14px}
  .contacts{left:161px;top:306px;list-style:none;color:var(--purple-deep);font-size:12.5px;font-weight:600}
  .contacts li{display:flex;align-items:center;gap:6px;height:20px}
  .contacts svg{width:13px;height:13px}
  .brand--classes{left:372px;top:322px;font-size:16px}
  .brand--classes .brand__dot{width:22px;height:22px}
</style>
</head>
<body>

<section class="card card--services">
  <svg class="bg" width="582" height="418" viewBox="0 0 582 418">
    <defs>
      <linearGradient id="panelGrad" x1="0" x2="1">
        <stop offset="0" stop-color="#4a1450"/><stop offset="1" stop-color="#7a2a6e"/>
      </linearGradient>
      <linearGradient id="photoGrad" x1="0" y1="0" x2="0" y2="1">
        <stop offset="0" stop-color="#c9a88a"/><stop offset=".6" stop-color="#a77a55"/><stop offset="1" stop-color="#8a5a36"/>
      </linearGradient>
    </defs>
    <rect x="0" y="133" width="400" height="197" fill="url(#panelGrad)"/>
    <g role="img" aria-label="Photo of a smiling bakery owner in an apron standing behind her wooden counter">
      <path d="M330 0 L582 0 L582 418 L330 418 C300 330 300 150 340 40 Z" fill="url(#photoGrad)"/>
    </g>
    <path d="M380 0 L400 0 C340 30 300 140 300 250 C300 330 320 390 340 418 L325 418 C305 380 288 320 288 250 C288 140 320 40 380 0 Z" fill="var(--gold)"/>
    <path d="M0 375 L200 375 L215 418 L0 418 Z" fill="var(--gold)"/>
  </svg>

  <div class="abs brand" style="left:23px;top:16px"><span class="brand__dot"></span>Lantern Ledger</div>
  <h1 class="abs headline">Small Business Accounting<br>Made Easy.</h1>
  <div class="abs tab tab--services">Bookkeeping &amp; CFO Services</div>
  <ul class="abs ticks ticks--services">
    <li>Monthly Reports and Statements</li>
    <li>Profit and Loss Statement</li>
    <li>Trial Balance</li>
    <li>Balance Sheet</li>
    <li>General Ledger Report</li>
    <li>Bank Reconciliation</li>
    <li>Payroll Reconciliation</li>
  </ul>
  <div class="abs tax-badge">Tax Planning &amp;<br>Tax Preparation<br>Services Available</div>
  <p class="abs schedule" style="left:13px;top:352px">Schedule Your Appointment</p>
  <p class="abs call" style="left:14px;top:384px">CALL (555) 214-0387</p>
  <p class="abs site" style="left:218px;top:392px">www.lanternledger.com</p>
</section>

<section class="card card--classes">
  <svg class="bg" width="582" height="418" viewBox="0 0 582 418">
    <defs>
      <linearGradient id="classGrad" x1="0" x2="1">
        <stop offset="0" stop-color="#4a1450"/><stop offset="1" stop-color="#6e2466"/>
      </linearGradient>
      <linearGradient id="deskGrad" x1="0" y1="0" x2="1" y2="1">
        <stop offset="0" stop-color="#f3f2f0"/><stop offset="1" stop-color="#d9d7d4"/>
      </linearGradient>
    </defs>
    <g role="img" aria-label="Soft background photo of a laptop keyboard and desk">
      <rect x="0" y="200" width="582" height="180" fill="url(#deskGrad)"/>
    </g>
    <path d="M0 12 L582 12 L582 212 C480 262 120 272 0 218 Z" fill="url(#classGrad)"/>
    <path d="M0 218 C120 272 480 262 582 212 L582 220 C480 270 120 280 0 226 Z" fill="var(--white)"/>
    <path d="M0 226 C120 280 480 270 582 220 L582 226 C480 277 120 287 0 232 Z" fill="var(--gold)"/>
    <rect x="0" y="379" width="582" height="39" fill="var(--white)"/>
    <path d="M372 379 L582 379 L582 418 L360 418 Z" fill="var(--gold)"/>
  </svg>

  <div class="abs tab tab--classes">The BookWise Cloud Classes</div>
  <div class="abs partner-badge" role="img" aria-label="BookWise Certified PRoMentor badge"></div>
  <p class="abs classes-lead">Learn any or all of the following from a<br>certified BookWise PRoMentor.</p>
  <ul class="abs ticks ticks--classes" style="left:25px;top:111px">
    <li>Navigate BookWise Cloud</li>
    <li>Set up Chart of Accounts</li>
    <li>Create &amp; Manage Vendors</li>
    <li>Create Purchase Orders</li>
  </ul>
  <ul class="abs ticks ticks--classes" style="left:300px;top:111px">
    <li class="ticks__small">Time Tracking for Employees &amp; Subcontractors</li>
    <li>Create customers &amp; Send Invoices</li>
    <li>Payroll</li>
    <li>Manage Bank Feeds</li>
  </ul>
  <div class="abs signup">
    <span>SIGN UP TO TAKE THE CLASSES:</span>
    <svg width="11" height="11" viewBox="0 0 12 12"><circle cx="6" cy="6" r="5" fill="none" stroke="#fff" stroke-width="1.2"/><ellipse cx="6" cy="6" rx="2.2" ry="5" fill="none" stroke="#fff" stroke-width="1"/><line x1="1" y1="6" x2="11" y2="6" stroke="#fff"/></svg>
    <span class="url">https://www.lanternledger.com/bookwise/</span>
  </div>
  <p class="abs delivery">Classes are taught virtually and in person</p>

  <div class="abs portrait" role="img" aria-label="Portrait photo of Doris Venn"></div>
  <p class="abs person">Doris Venn EA</p>
  <ul class="abs contacts">
    <li><svg viewBox="0 0 14 14"><circle cx="7" cy="7" r="7" fill="var(--gold)"/><path d="M4.5 3.5 L6 3.5 L6.5 5.5 L5.6 6.2 C6 7.3 6.8 8.1 7.8 8.5 L8.5 7.6 L10.5 8 L10.5 9.5 C7 10 4 7 4.5 3.5 Z" fill="#fff"/></svg>(555) 214-0387</li>
    <li><svg viewBox="0 0 14 14"><circle cx="7" cy="7" r="7" fill="var(--gold)"/><rect x="3.5" y="4.5" width="7" height="5" fill="#fff"/><path d="M3.5 4.5 L7 7.3 L10.5 4.5" fill="none" stroke="var(--gold)" stroke-width=".9"/></svg>doris.venn@lanternledger.com</li>
    <li><svg viewBox="0 0 14 14"><circle cx="7" cy="7" r="7" fill="var(--gold)"/><circle cx="7" cy="7" r="3.8" fill="none" stroke="#fff"/><line x1="3.2" y1="7" x2="10.8" y2="7" stroke="#fff" stroke-width=".8"/><ellipse cx="7" cy="7" rx="1.6" ry="3.8" fill="none" stroke="#fff" stroke-width=".8"/></svg>www.lanternledger.com</li>
  </ul>
  <div class="abs brand brand--classes"><span class="brand__dot"></span>Lantern Ledger</div>

  <p class="abs schedule" style="left:13px;top:393px;display:flex;align-items:center;gap:6px">Schedule Your Appointment
    <svg width="12" height="12" viewBox="0 0 12 12"><circle cx="6" cy="6" r="6" fill="var(--purple-deep)"/><circle cx="6" cy="6" r="3.4" fill="none" stroke="#fff" stroke-width=".9"/><line x1="2.6" y1="6" x2="9.4" y2="6" stroke="#fff" stroke-width=".8"/></svg>
    <span style="font-size:12.5px;text-transform:none">www.lanternledger.com</span></p>
  <p class="abs call" style="left:385px;top:386px">CALL (555) 214-0387</p>
</section>

</body>
</html>
```